Waste Oil Filter collection & disposal

Basically I need a 1 page website for the business called Brenmoor Waste Solutions.
We are a environmental service provider and we collect and dispose of waste oil filters to protect the environment from hazardous waste oil products.

This is the link to our current website: www.brenmoorwaste.co.nz

we want it to look fresh and better than our current website. we may potentially look at getting a new logo designed and are open to ideas/designs if you have any.

Industry/Entity Type

Business

Logo Text

Brenmoor Waste Solutions

Number of Pages Required

1 page

Requirements
Must have
• same colours as current website.
• description of what service we provide please refer to leaflet attached

```html
<!DOCTYPE html>
<html lang="en">
<head>
<meta charset="utf-8">
<title>Brenmoor Waste Solutions Ltd</title>
<link href="https://fonts.googleapis.com/css2?family=Lato:wght@400;700&family=Open+Sans:wght@400;600&display=swap" rel="stylesheet">
<style>
:root{
  --green:#3dba3d;
  --dark:#333333;
  --text:#4a4a4a;
  --muted:#6f6f6f;
  --light:#efefef;
  --white:#ffffff;
}
*{margin:0;padding:0;box-sizing:border-box}
html,body{width:1200px;height:3303px;overflow:hidden;background:var(--white)}
body{position:relative;font-family:"Open Sans",Arial,sans-serif;color:var(--text)}
.abs{position:absolute}
.heading{font-family:"Lato",Arial,sans-serif;font-weight:700;color:#555;text-transform:uppercase;font-size:28px;letter-spacing:.5px}
.center{text-align:center;left:0;width:1200px}
.rule{position:absolute;height:3px;background:var(--green);width:56px}
/* header */
.brand{left:77px;top:30px;display:flex;align-items:center;gap:12px;font-family:"Lato",sans-serif;font-weight:700;font-size:20px;color:var(--dark)}
.brand-mark{width:26px;height:26px;border-radius:50%;background:var(--green)}
.nav{top:40px;font-family:"Lato",sans-serif;font-size:18px;color:#555}
.nav-about{left:793px}
.nav-about::after{content:"";position:absolute;left:0;top:34px;width:56px;height:3px;background:var(--green)}
.nav-gallery{left:889px}
.btn-contact{left:988px;top:29px;width:135px;height:50px;background:var(--green);color:#fff;font-family:"Lato",sans-serif;font-weight:700;font-size:17px;display:flex;align-items:center;justify-content:center;border-radius:3px}
/* hero */
.hero-title{left:77px;top:200px;font-family:"Lato",sans-serif;font-weight:700;font-size:47px;color:#555}
.hero-sub{left:77px;top:276px;font-family:"Lato",sans-serif;font-weight:700;font-size:21px;line-height:31px;color:#444;width:560px}
.hero-product{left:575px;top:176px;width:625px;height:385px}
.backdrop{left:0;top:560px;width:1200px;height:740px}
/* about */
.about-card{left:183px;top:561px;width:834px;height:188px;background:#fff;box-shadow:0 2px 14px rgba(0,0,0,.15);border-radius:4px;text-align:center}
.about-card .heading{margin-top:40px}
.about-card p{width:680px;margin:30px auto 0;font-size:15.5px;line-height:26px;color:var(--muted)}
.values{top:826px;left:0;width:1200px}
.value{position:absolute;width:230px;text-align:center;font-size:15.5px;line-height:25px;color:var(--muted)}
.value-icon{width:84px;height:84px;margin:0 auto 22px;border-radius:50%;background:#fff;box-shadow:0 2px 10px rgba(0,0,0,.15);display:flex;align-items:center;justify-content:center}
/* service */
.service-title{left:79px;top:1158px;color:var(--green)}
.service-line{left:77px;top:1205px;width:495px;height:3px;background:var(--green)}
.service-name{left:79px;top:1234px;font-family:"Lato",sans-serif;font-size:21px;color:#555}
.service-text{left:79px;top:1276px;width:490px;font-size:15.5px;line-height:28px;color:var(--muted)}
.truck-card{left:599px;top:1074px;width:524px;height:326px;background:#fff;border-radius:30px;box-shadow:0 2px 14px rgba(0,0,0,.18)}
.truck-photo{left:656px;top:1088px;width:414px;height:300px;background:linear-gradient(180deg,#7f9a6e 0%,#4f7a55 45%,#2f8a62 65%,#6d6d68 100%);border-radius:4px}
/* oil */
.oil-text{top:1554px;font-size:15.5px;line-height:27px;color:var(--muted)}
.divider{left:77px;top:1655px;width:1046px;height:2px;background:#e2e2e2}
/* gallery */
.gallery-item{top:1805px;width:240px;height:157px}
.g1,.g4{background:linear-gradient(160deg,#6f7c78,#3f5d52 55%,#2d4a40)}
.g2{background:linear-gradient(180deg,#566a8a,#3b4f72 45%,#6e6f6f)}
.g3{background:linear-gradient(180deg,#5d7a55,#2e8a62 55%,#5b5b58)}
.arrow{position:absolute}
/* process */
.step{position:absolute;width:159px;height:92px;background:#fff;border-radius:4px;box-shadow:0 2px 10px rgba(0,0,0,.15);text-align:center}
.step b{display:block;font-family:"Lato",sans-serif;font-weight:400;font-size:29px;color:var(--green);margin-top:12px}
.step span{display:block;font-size:14.5px;color:var(--muted);margin-top:4px}
/* testimonial */
.quote-band{left:0;top:2345px;width:1200px;height:320px;background:var(--light)}
.quote-text{top:2504px;font-size:18px;color:#555}
.quote-author{top:2552px;font-family:"Lato",sans-serif;font-weight:700;font-size:20px;color:#444}
.dots{top:2603px;left:562px;display:flex;gap:14px}
.dots i{width:16px;height:16px;border-radius:50%;background:#cfcfcf}
.dots i.on{background:var(--green)}
/* pricing */
.price{top:2682px;width:324px;height:165px;background:#fff;border-radius:4px;box-shadow:0 2px 12px rgba(0,0,0,.16);text-align:center}
.price strong{display:block;font-family:"Lato",sans-serif;font-weight:700;font-size:44px;color:#555;margin-top:32px}
.price em{display:block;width:56px;height:3px;background:var(--green);margin:14px auto 0}
.price span{display:block;font-family:"Lato",sans-serif;font-size:21px;color:#555;margin-top:16px}
/* footer */
.footer{left:0;top:2917px;width:1200px;height:324px;background:var(--dark);color:#fff}
.footer-title{position:absolute;top:42px;left:0;width:1200px;text-align:center;font-family:"Lato",sans-serif;font-weight:700;font-size:26px}
.footer-rule{left:572px;top:88px}
.col{position:absolute;top:127px;font-size:15px;line-height:29px}
.col h4{font-family:"Lato",sans-serif;font-weight:700;font-size:20px;margin-bottom:18px}
.contact-row{display:flex;align-items:center;gap:14px}
.map{width:220px;height:100px;background:linear-gradient(135deg,#e9ece8,#dfe4e2);border-radius:2px;margin-top:0}
.copyright{left:0;top:3241px;width:1200px;height:62px;background:var(--green);color:#2a2a2a;font-size:15px;display:flex;align-items:center;justify-content:center}
</style>
</head>
<body>

<header>
  <div class="abs brand"><span class="brand-mark"></span>Brenmoor Waste Solutions</div>
  <nav>
    <span class="abs nav nav-about">ABOUT</span>
    <span class="abs nav nav-gallery">GALLARY</span>
    <span class="abs btn-contact">CONTACT US</span>
  </nav>
</header>

<svg class="abs backdrop" viewBox="0 0 1200 740" aria-hidden="true">
  <polygon points="0,40 1200,0 1200,250 0,130" fill="#f3f3f3"/>
  <polygon points="0,130 1200,250 1200,430 0,260" fill="#ececec"/>
  <polygon points="0,260 650,360 0,540" fill="#f0f0f0"/>
  <polygon points="650,360 1200,430 1200,520" fill="#f5f5f5"/>
</svg>

<section class="hero">
  <h1 class="abs hero-title">Brenmoor Waste Solutions Ltd</h1>
  <p class="abs hero-sub">specialize in the collection &amp; disposal of oil / fuel filters, servicing the lower north island on a monthly cycle.</p>
  <svg class="abs hero-product" viewBox="0 0 625 385" role="img" aria-label="Photo of two black oil filters">
    <defs>
      <linearGradient id="filterTone" x1="0" x2="1">
        <stop offset="0" stop-color="#1a1a1a"/><stop offset=".5" stop-color="#4a4a4a"/><stop offset="1" stop-color="#111"/>
      </linearGradient>
    </defs>
    <rect x="10" y="110" width="360" height="220" rx="110" fill="url(#filterTone)"/>
    <rect x="375" y="10" width="245" height="370" rx="60" fill="url(#filterTone)"/>
  </svg>
</section>

<section class="about">
  <div class="abs about-card">
    <h2 class="heading">About Us</h2>
    <span class="rule" style="left:389px;top:90px"></span>
    <p>We offer a cost effective environmentally friendly system for the collection and disposal of waste oil filters helping minimise contamination of landfills keeping your industry compliant.</p>
  </div>
  <div class="abs values">
    <div class="value" style="left:85px">
      <div class="value-icon"><svg width="42" height="42" viewBox="0 0 42 42"><path d="M21 5 L29 18 H13 Z M7 33 L14 20 L22 33 Z M35 33 H20 L28 20 Z" fill="var(--green)"/></svg></div>
      We are passionate about doing our bit in keeping New Zealand Clean and Green
    </div>
    <div class="value" style="left:354px">
      <div class="value-icon"><svg width="42" height="42" viewBox="0 0 42 42"><circle cx="21" cy="21" r="16" fill="none" stroke="var(--green)" stroke-width="4"/><path d="M5 21 H37 M21 5 V37" stroke="var(--green)" stroke-width="3"/></svg></div>
      Our processes are environmentally friendly and minimise the contamination of landfills.
    </div>
    <div class="value" style="left:620px">
      <div class="value-icon"><svg width="42" height="42" viewBox="0 0 42 42"><circle cx="21" cy="21" r="15" fill="var(--green)"/><circle cx="21" cy="21" r="6" fill="#fff"/></svg></div>
      We offer a cost effective system for the collection and disposal of waste oil filters
    </div>
    <div class="value" style="left:889px">
      <div class="value-icon"><svg width="42" height="42" viewBox="0 0 42 42"><path d="M8 36 V14 H14 V22 L22 16 V22 L30 16 V8 H35 V36 Z" fill="var(--green)"/></svg></div>
      We keep your industry compliant.
    </div>
  </div>
</section>

<section class="service">
  <h2 class="abs heading service-title">Service We Provide</h2>
  <span class="abs service-line"></span>
  <h3 class="abs service-name">Brenmoor Waste Service</h3>
  <p class="abs service-text">Brenmoor Waste Solutions Ltd service the Lower North Island and specialise in the collection &amp; disposal of oil &amp; fuel filters</p>
  <div class="abs truck-card"></div>
  <div class="abs truck-photo" role="img" aria-label="Photo of the green and white collection truck"></div>
</section>

<section class="oil">
  <h2 class="abs heading center" style="top:1487px">What Happens To The Oil</h2>
  <span class="rule" style="left:572px;top:1530px"></span>
  <p class="abs center oil-text">All residual oil is collected into our tank and then recycled. Currently we are<br>processing over 2,000 litres of oil a month</p>
  <div class="abs divider"></div>
</section>

<section class="gallery">
  <h2 class="abs heading center" style="top:1727px">Our Gallary</h2>
  <span class="rule" style="left:572px;top:1770px"></span>
  <svg class="arrow" style="left:46px;top:1870px" width="16" height="30" viewBox="0 0 16 30"><path d="M14 2 L2 15 L14 28" fill="none" stroke="var(--green)" stroke-width="2.5"/></svg>
  <div class="abs gallery-item g1" style="left:77px" role="img" aria-label="Photo of filters on the processing line"></div>
  <div class="abs gallery-item g2" style="left:346px" role="img" aria-label="Photo of collected filters stacked on racks"></div>
  <div class="abs gallery-item g3" style="left:614px" role="img" aria-label="Photo of the collection truck"></div>
  <div class="abs gallery-item g4" style="left:883px" role="img" aria-label="Photo of filters on the processing line"></div>
  <svg class="arrow" style="left:1136px;top:1870px" width="16" height="30" viewBox="0 0 16 30"><path d="M2 2 L14 15 L2 28" fill="none" stroke="var(--green)" stroke-width="2.5"/></svg>
</section>

<section class="process">
  <h2 class="abs heading center" style="top:2055px">Process</h2>
  <span class="rule" style="left:572px;top:2098px"></span>
  <div class="step" style="left:77px;top:2178px"><b>01</b><span>Drained</span></div>
  <div class="step" style="left:255px;top:2136px"><b>02</b><span>Sorted</span></div>
  <div class="step" style="left:434px;top:2178px"><b>03</b><span>Drained again</span></div>
  <div class="step" style="left:612px;top:2136px"><b>04</b><span>Crushed into bricks</span></div>
  <div class="step" style="left:788px;top:2178px"><b>05</b><span>Drained 3rd time</span></div>
  <div class="step" style="left:964px;top:2136px"><b>06</b><span>Metal Recycling</span></div>
</section>

<section class="testimonial">
  <div class="abs quote-band"></div>
  <svg class="abs" style="left:568px;top:2405px" width="64" height="48" viewBox="0 0 64 48"><path d="M0 48 V22 Q0 2 24 0 V10 Q12 12 12 22 H26 V48 Z M36 48 V22 Q36 2 60 0 V10 Q48 12 48 22 H62 V48 Z" fill="#c8c8c8"/></svg>
  <svg class="arrow" style="left:77px;top:2519px" width="16" height="30" viewBox="0 0 16 30"><path d="M14 2 L2 15 L14 28" fill="none" stroke="var(--green)" stroke-width="2.5"/></svg>
  <p class="abs center quote-text">each used oil filter has onaver age, more than quarter of a litre of used motor oil</p>
  <p class="abs center quote-author">- GreenCycle Trust</p>
  <div class="abs dots"><i></i><i></i><i class="on"></i></div>
  <svg class="arrow" style="left:1107px;top:2519px" width="16" height="30" viewBox="0 0 16 30"><path d="M2 2 L14 15 L2 28" fill="none" stroke="var(--green)" stroke-width="2.5"/></svg>
</section>

<section class="pricing">
  <div class="abs price" style="left:77px"><strong>$65.00</strong><em></em><span>Monthly Bin Collection</span></div>
  <div class="abs price" style="left:438px"><strong>$35.00</strong><em></em><span>Additional Bins</span></div>
  <div class="abs price" style="left:799px"><strong>$85.00</strong><em></em><span>Account Set Up Fee</span></div>
</section>

<footer class="abs footer">
  <h2 class="footer-title">READY TO HELP YOU</h2>
  <span class="rule footer-rule"></span>
  <div class="col" style="left:79px">
    <h4>OPNING HOURS</h4>
    <p>Monday - Friday<br>7.30am - 5.00pm</p>
  </div>
  <div class="col" style="left:440px">
    <h4>CONTACT INFO</h4>
    <p class="contact-row" style="margin-left:0"><svg width="20" height="18" viewBox="0 0 20 18"><path d="M3 1 L7 1 L8 5 L6 7 Q8 11 12 13 L14 11 L18 12 L18 16 Q10 18 5 12 Q1 7 3 1 Z" fill="var(--green)"/></svg>info@brenmoorwaste.co.nz</p>
    <p class="contact-row"><svg width="20" height="16" viewBox="0 0 20 16"><rect x="1" y="2" width="18" height="12" fill="none" stroke="var(--green)" stroke-width="2"/><path d="M1 2 L10 9 L19 2" fill="none" stroke="var(--green)" stroke-width="2"/></svg>06 555 0148</p>
  </div>
  <div class="col" style="left:799px">
    <h4>MAP</h4>
    <div class="map" role="img" aria-label="Street map showing the depot location"></div>
  </div>
</footer>

<div class="abs copyright">©BRENMOOR WASTE SOLUTIONS LTD. 2017 - All Rights Reserved.</div>

</body>
</html>
```